TRNV LLP website - revamping our website after 23 years

Our website needs a complete overhaul. The purpose of this exercise is to provide us with your vision of what you think the website should look like. We don't need the website to be created or coded. Just need creative designs.

We have a four sites that we would like to base our website on;

We like the simplicity of Fairwicks, the style of Pemberly Strand and Kettridge.

http://www.pemberlystrand-example.com/en/toronto-ontario/
http://www.fairwicks-example.ca/
hallkettridge-example.com
http://www.vendrupe-example.com/our-professionals.html

We have a logo that we would like to use which will be attached below. We need to keep our website looking very professional as we have a large number of high net worth clients.
Updates

Hi, We've received some good website designs but they appear to be the same type of template websites we've received in the past - this is not what we're looking for. What we want is a unique website that is modelled on the following three company websites: http://www.fairwicks-example.ca/ www.hallkettridge-example.com/ http://www.pemberlystrand-example.com/en/toronto-ontario/

Thank you everyone for your designs. I will be posting updates and my comments on the various designs in the next day - I want to thank you for the creative designs I see. I thought i would explain a bit about our firm and perhaps it can help when you design the theme of our website: - Our firm is like a family and our clients are truly like our friends. We have close knit relationships in and outside of the office with staff and clients. - We are an 'out of the box' type of firm. We operate differently than most firms and that's a differentiating factor in what makes us who we are - Our slogan is "Count on us" which is a testament to the way we run our practice - We would like an open, fresh, clean look to our website - we don't want the landing page to be overly long or complex because we have limited time to update the website and limited content That's it for the time being - when things come to mind I will post them here.

Can we try a design as follows: - make the website look very similar to www.fairwicks-example.ca - use the same background colour - Keep the same black top but insert our logo - incorporate some of the content from our current website www.trnv-example.com

I have been away dealing with a personal matter. I will look into these websites tomorrow afternoon and provide more feedback / info on the top designer. Thank you

Hi designers, I want to apologize for the delay. I plan on wrapping things up within the next few days. I will go through a few of the top designs and offer my comments. Thank you for your patience.

Target Market(s)

Mainly our current clients - We have a large number of high net worth individuals as clients.

Industry/Entity Type

Accounting

Number of Pages Required

1 page

Requirements
Must have
• Please model website on the websites indicated above.
• Our current website is www.trnv-example.com. It's dark, cluttered and not inviting. We want a fresh, clean website. Please incorporate the logo's attached below.

```html
<!DOCTYPE html>
<html lang="en">
<head>
<meta charset="utf-8">
<title>TRNV LLP Chartered Professional Accountants</title>
<link href="https://fonts.googleapis.com/css2?family=Cinzel:wght@400;600&family=Lato:ital,wght@0,400;0,700;1,400;1,700&display=swap" rel="stylesheet">
<style>
:root{
  --blue:#29a8e0;
  --blue-dark:#1d8fc2;
  --charcoal:#3a3a3c;
  --ink:#2b2b2d;
  --text:#444;
  --white:#fff;
  --rule:#d9d9d9;
}
*{margin:0;padding:0;box-sizing:border-box}
html,body{width:1200px;height:2466px;overflow:hidden}
body{font-family:"Lato",sans-serif;color:var(--text);background:var(--white);position:relative}
.abs{position:absolute}
.serif{font-family:"Cinzel",serif}

/* top bar */
.topbar{left:0;top:0;width:1200px;height:33px;background:var(--blue);color:var(--white);font-size:16px}
.topbar .item{position:absolute;top:6px;display:flex;align-items:center;gap:8px}

/* header */
.header{left:0;top:33px;width:1200px;height:140px;background:var(--charcoal);border-bottom:2px solid #555}
.brand{position:absolute;left:80px;top:70px;display:flex;flex-direction:column}
.brand-row{display:flex;align-items:center;gap:10px}
.brand-mark{width:18px;height:18px;background:var(--blue)}
.brand-name{font-family:"Cinzel",serif;font-size:34px;color:var(--white);letter-spacing:1px}
.brand-sub{font-size:8.5px;color:#bbb;letter-spacing:1.3px;text-transform:uppercase;margin-top:2px}
.nav{position:absolute;left:350px;top:93px;display:flex;align-items:center}
.nav a{font-family:"Cinzel",serif;font-size:17px;color:var(--white);text-decoration:none;padding:0 21px;border-left:1px solid #666;line-height:18px}
.nav a:first-child{border-left:none;color:var(--blue);border-bottom:2px solid var(--blue);padding-bottom:4px}

/* hero */
.hero{left:0;top:173px;width:1200px;height:444px;background:radial-gradient(ellipse at 48% 38%,#b7832a 0%,#5a3c16 22%,#1c1611 55%,#0d0b0a 100%)}
.hero-caption{left:0;top:526px;width:1200px;height:91px;background:rgba(20,18,16,.72);color:var(--white);text-align:center;font-family:"Cinzel",serif;font-size:27px;line-height:35px;padding-top:10px;letter-spacing:.5px}
.arrow{position:absolute}

/* welcome */
.welcome-title{left:0;top:655px;width:1200px;text-align:center;font-family:"Cinzel",serif;font-size:34px;color:var(--ink)}
.welcome-title span{color:var(--blue)}
.title-mark{display:inline-block;width:26px;height:26px;background:var(--blue);transform:rotate(45deg);margin-right:18px;vertical-align:-2px}
.welcome-rule{left:110px;top:725px;width:980px;height:1px;background:var(--rule)}
.welcome-rule-accent{left:525px;top:723px;width:150px;height:3px;background:var(--blue)}
.welcome-text{left:95px;top:757px;width:1010px;text-align:center;font-size:14.5px;line-height:27px;color:#333}
.btn{left:536px;top:856px;width:127px;height:39px;border:1.5px solid var(--blue);color:var(--blue);font-size:15px;display:flex;align-items:center;justify-content:center}

/* services */
.services{left:0;top:938px;width:1200px;height:654px;background:linear-gradient(135deg,#2f3237 0%,#555b63 45%,#3b3e44 100%)}
.section-title{position:absolute;left:0;width:1200px;text-align:center;font-family:"Cinzel",serif;font-size:35px}
.section-rule{position:absolute;left:82px;width:1036px;height:1px}
.section-diamond{position:absolute;left:590px;width:20px;height:20px;transform:rotate(45deg)}
.tile{position:absolute;width:311px;height:209px;border:1px solid #bbb;overflow:hidden}
.tile .photo{width:100%;height:100%}
.tile .label{position:absolute;left:0;bottom:0;width:100%;height:46px;background:rgba(20,20,20,.72);color:var(--white);font-family:"Cinzel",serif;font-size:18px;display:flex;align-items:center;justify-content:center;letter-spacing:.5px}

/* testimonials */
.testimonials{left:0;top:1592px;width:1200px;height:348px;background:var(--blue)}
.portrait{position:absolute;left:117px;top:1756px;width:112px;height:112px;transform:rotate(45deg);border:6px solid var(--white);background:linear-gradient(135deg,#c9cfd6,#5d6670)}
.quote{left:296px;top:1754px;width:812px;color:var(--white);font-style:italic;font-size:14.5px;line-height:25px}
.quote-mark{font-family:"Cinzel",serif;font-size:30px;font-style:normal;line-height:0;vertical-align:-10px;opacity:.85}
.quote-name{left:296px;top:1872px;color:var(--white);font-style:italic;font-weight:700;font-size:18px}

/* map */
.map{left:0;top:1940px;width:1200px;height:312px;background:linear-gradient(160deg,#efe9dc 0%,#e6dfcf 50%,#ede6d6 100%)}
.map-card{left:638px;top:2030px;width:274px;height:91px;background:var(--white);box-shadow:0 2px 6px rgba(0,0,0,.25);padding:12px 16px}
.map-card h4{font-family:"Cinzel",serif;font-size:16px;font-weight:600;color:#222;margin-bottom:6px}
.map-card p{font-size:12px;line-height:19px;color:#444}

/* footer */
.footer-info{left:0;top:2252px;width:1200px;height:120px;background:linear-gradient(90deg,#2b3440,#3b4654 50%,#2b3440)}
.info{position:absolute;top:2276px;display:flex;gap:14px;color:var(--white)}
.info h5{font-family:"Cinzel",serif;font-size:14.5px;font-weight:600;letter-spacing:.5px;margin-bottom:4px}
.info p{font-size:12.5px;line-height:18px;color:#ccd}
.footer-nav{left:0;top:2372px;width:1200px;height:48px;background:var(--blue);display:flex;justify-content:center;align-items:center}
.footer-nav a{color:var(--white);font-size:15px;font-weight:700;text-decoration:none;padding:0 27px;border-left:1px solid rgba(255,255,255,.45);line-height:20px}
.footer-nav a:first-child{border-left:none}
.copyright{left:0;top:2420px;width:1200px;height:46px;background:var(--ink);color:#ddd;font-size:12px;display:flex;align-items:center;justify-content:center}
</style>
</head>
<body>

<div class="abs topbar">
  <div class="item" style="left:784px">
    <svg width="20" height="14" viewBox="0 0 20 14"><rect x="1" y="1" width="18" height="12" fill="none" stroke="#fff" stroke-width="1.5"/><path d="M1 1l9 7 9-7" fill="none" stroke="#fff" stroke-width="1.5"/></svg>
    info@trnv-example.com
  </div>
  <div class="item" style="left:980px">
    <svg width="14" height="16" viewBox="0 0 14 16"><path d="M3 1l3 3-2 2c1 2 3 4 5 5l2-2 3 3-2 3C6 15-1 8 1 3z" fill="#fff"/></svg>
    (416) 555-0140
  </div>
</div>

<header class="abs header">
  <div class="brand">
    <div class="brand-row"><span class="brand-mark"></span><span class="brand-name">TRNV LLP</span></div>
    <span class="brand-sub">Chartered Professional Accountants</span>
  </div>
  <nav class="nav">
    <a href="#">Home</a><a href="#">About Us</a><a href="#">Services</a><a href="#">Library</a><a href="#">Links</a><a href="#">Careers</a><a href="#">Contact Us</a>
  </nav>
</header>

<div class="abs hero" role="img" aria-label="Hand holding a glowing globe linked by a network of business icons"></div>
<svg class="arrow" style="left:30px;top:372px" width="24" height="44" viewBox="0 0 24 44"><path d="M22 2L3 22l19 20" fill="none" stroke="#ccc" stroke-width="2"/></svg>
<svg class="arrow" style="left:1146px;top:372px" width="24" height="44" viewBox="0 0 24 44"><path d="M2 2l19 20L2 42" fill="none" stroke="#ccc" stroke-width="2"/></svg>
<div class="abs hero-caption">Together, We Bring Over 100 Years of Valuable Wxperience to the<br>Practice of Publick Accounting.</div>

<h1 class="abs welcome-title"><span class="title-mark"></span>Welcome To <span>TRNV LLP</span></h1>
<div class="abs welcome-rule"></div>
<div class="abs welcome-rule-accent"></div>
<p class="abs welcome-text">Lorem ipsum dolor sit amet, consectetuer adipiscing elit, sed diam nonummy nibh euismod tincidunt uti laoreet dolore magna aliquam erat volutpat. Ut wisi enim ad minim veniam, quis nostrud exerci tationok ullamcorper suscipit lobortis nisl ut aliquip ex ea commodo consequat. Duis autem vel eum iriure dolorn in hendrerit in vulputate velit esse molestie consequat, vel illum dolore eu feugiat nulla facilisis at verom .</p>
<div class="abs btn">Read More</div>

<section class="abs services" role="img" aria-label="Blurred backdrop of a calculator and financial papers"></section>
<h2 class="section-title" style="top:980px;color:#fff">Our Services</h2>
<div class="section-rule" style="top:1052px;background:rgba(255,255,255,.35)"></div>
<div class="section-diamond" style="top:1042px;border:2px solid #fff;background:#4a4e55"></div>
<svg class="arrow" style="left:30px;top:1316px" width="22" height="40" viewBox="0 0 22 40"><path d="M20 2L3 20l17 18" fill="none" stroke="#ddd" stroke-width="2"/></svg>
<svg class="arrow" style="left:1148px;top:1316px" width="22" height="40" viewBox="0 0 22 40"><path d="M2 2l17 18L2 38" fill="none" stroke="#ddd" stroke-width="2"/></svg>

<div class="tile" style="left:94px;top:1090px"><div class="photo" role="img" aria-label="Calculator and pen on a financial spreadsheet" style="background:linear-gradient(135deg,#dfe7ef,#8fa3b8)"></div><div class="label">Accounting And Auditing</div></div>
<div class="tile" style="left:444px;top:1090px"><div class="photo" role="img" aria-label="Business people reviewing charts at a desk" style="background:linear-gradient(135deg,#e8ecf1,#9aa7b6)"></div><div class="label">Business Advisory</div></div>
<div class="tile" style="left:796px;top:1090px"><div class="photo" role="img" aria-label="Blue jigsaw puzzle pieces" style="background:linear-gradient(135deg,#cfe3f3,#4f86b5)"></div><div class="label">Due Diligence</div></div>
<div class="tile" style="left:94px;top:1338px"><div class="photo" role="img" aria-label="Person working at a desk with a laptop and notes" style="background:linear-gradient(135deg,#c9b79a,#6e5a44)"></div><div class="label">High-Tech Industry</div></div>
<div class="tile" style="left:444px;top:1338px"><div class="photo" role="img" aria-label="Medical professionals in conversation" style="background:linear-gradient(135deg,#f1f2f4,#8d939c)"></div><div class="label">Medical Professionals</div></div>
<div class="tile" style="left:796px;top:1338px"><div class="photo" role="img" aria-label="Fountain pen and glasses on a tax form" style="background:linear-gradient(135deg,#d4e0ec,#5c7896)"></div><div class="label">Personal Tax Services</div></div>

<section class="abs testimonials"></section>
<h2 class="section-title" style="top:1630px;color:#2b2b2d">Clients Testimonials</h2>
<div class="section-rule" style="top:1698px;background:rgba(255,255,255,.45)"></div>
<div class="section-diamond" style="top:1688px;border:2px solid #fff;background:var(--blue)"></div>
<svg class="arrow" style="left:30px;top:1793px" width="22" height="40" viewBox="0 0 22 40"><path d="M20 2L3 20l17 18" fill="none" stroke="#fff" stroke-width="2"/></svg>
<svg class="arrow" style="left:1148px;top:1793px" width="22" height="40" viewBox="0 0 22 40"><path d="M2 2l17 18L2 38" fill="none" stroke="#fff" stroke-width="2"/></svg>
<div class="portrait" role="img" aria-label="Portrait of a client in a business suit"></div>
<p class="abs quote"><span class="quote-mark">“</span> Lorem ipsum dolor sit amet, consectetuer adipiscing elit, sed diam nonummy nibh euismod tincidunt ut laoreet dolore kog magna aliquam erat volutpat. Ut wisi enim ad minim veniam, quis nostrud exerci tation ullamcorper suscipit lobortis nisl utvm aliquip ex ea commodo consequat. Duis autem vel eum iriure dolor in hendrerit in vulputate velit esse molestie consequat, veli illum dolore eu feugiat nulla facilisis at vero eros et accumsan et iusto. <span class="quote-mark">”</span></p>
<p class="abs quote-name">- Lorem ipsum</p>

<div class="abs map" role="img" aria-label="Street map showing the office location"></div>
<svg class="abs" style="left:578px;top:2128px" width="18" height="26" viewBox="0 0 18 26"><path d="M9 25C3 15 1 12 1 9a8 8 0 0116 0c0 3-2 6-8 16z" fill="#e8706a"/><circle cx="9" cy="9" r="3" fill="#fff"/></svg>
<div class="abs map-card">
  <h4>TRNV LLP</h4>
  <p>Suite 1200, 88 Larchmere Avenue, Toronto,<br>Ontario, Canada, M2N 0A1</p>
</div>

<footer>
  <div class="abs footer-info"></div>
  <div class="info" style="left:116px">
    <svg width="42" height="44" viewBox="0 0 42 44"><path d="M21 30C13 19 11 16 11 12a10 10 0 0120 0c0 4-2 7-10 18z" fill="#fff"/><circle cx="21" cy="12" r="4" fill="#3b4654"/><path d="M2 42l8-12h22l8 12z" fill="none" stroke="#fff" stroke-width="2"/></svg>
    <div><h5>TRNV LLP Chartered Accountants</h5><p>Suite 1200, 88 Larchmere Avenue, Toronto,<br>Ontario, Canada, M2N 0A1</p></div>
  </div>
  <div class="info" style="left:542px">
    <svg width="36" height="42" viewBox="0 0 36 42"><path d="M8 2l7 8-4 5c2 5 6 9 11 12l5-4 8 7-4 7C14 40 0 24 4 6z" fill="#fff"/></svg>
    <div><h5>Feel Free to Call Us Now</h5><p>(416) 555-0140<br>(416) 555-0190</p></div>
  </div>
  <div class="info" style="left:886px">
    <svg width="40" height="40" viewBox="0 0 40 40"><rect x="2" y="6" width="36" height="32" fill="none" stroke="#fff" stroke-width="2.5"/><rect x="2" y="6" width="36" height="7" fill="#fff"/><path d="M10 2v8M30 2v8" stroke="#fff" stroke-width="3"/><g fill="#fff"><rect x="8" y="18" width="5" height="5"/><rect x="17" y="18" width="5" height="5"/><rect x="26" y="18" width="5" height="5"/><rect x="8" y="27" width="5" height="5"/><rect x="17" y="27" width="5" height="5"/><rect x="26" y="27" width="5" height="5"/></g></svg>
    <div><h5>Working Hours</h5><p>Mon-Fri 9.00am - 4.00pm<br>Sunday: Closed</p></div>
  </div>
  <nav class="abs footer-nav">
    <a href="#">Home</a><a href="#">About Us</a><a href="#">SERVICES</a><a href="#">LIBRARY</a><a href="#">LINKS</a><a href="#">CAREERS</a><a href="#">Contact Us</a>
  </nav>
  <div class="abs copyright">Copyright © 2015 TRNV LLP Chartered Accountants | All Right Reserved.</div>
</footer>

</body>
</html>
```